Corvexa New Website

We are looking for a designer to provide html and css designs for a fiber to the home company. We are changing from our previous Talvorne Communications to Corvexa Communications, and will be using the attached logo now. Our current site can be seen at http://www.talvorne-example.com

Target Market(s)

Cable TV, Internet and Home Phone

Coding

Coded - Design and coding required

Number of Pages Required

1 page

```html
<!DOCTYPE html>
<html lang="en">
<head>
<meta charset="utf-8">
<title>Corvexa Communications</title>
<link href="https://fonts.googleapis.com/css2?family=Merriweather:wght@400;700&family=Roboto:wght@400;500;700&display=swap" rel="stylesheet">
<style>
:root{
  --orange:#f7952c;
  --blue:#1a5fa8;
  --navy:#2b3e52;
  --ink:#333;
  --muted:#9a9a9a;
  --white:#fff;
}
*{box-sizing:border-box;margin:0;padding:0}
html,body{width:1152px;height:1200px;overflow:hidden;background:var(--white)}
body{position:relative;font-family:'Roboto',Arial,sans-serif;color:var(--ink)}
.abs{position:absolute}
.site-header{left:0;top:0;width:1152px;height:74px}
.brand{left:90px;top:24px;display:flex;align-items:center;gap:8px;font-family:'Roboto',sans-serif;font-weight:700;font-size:20px;color:var(--blue)}
.brand-dot{width:14px;height:14px;border-radius:50%;background:var(--orange)}
.main-nav a{position:absolute;top:24px;font-size:13px;color:var(--ink);text-decoration:none;white-space:nowrap}
.main-nav a.active{color:var(--blue)}
.btn{display:flex;align-items:center;justify-content:center;background:var(--orange);color:var(--white);font-weight:700;font-size:15px;border-radius:20px;text-decoration:none}
.header-cta{left:897px;top:12px;width:132px;height:40px}
.hero{left:0;top:74px;width:1152px;height:452px;background:radial-gradient(ellipse at 55% 40%,#7a5a4a 0%,#4f3d33 40%,#2c2723 100%)}
.hero-badge{left:484px;top:185px;width:184px;height:28px;background:var(--orange);color:var(--white);font-family:'Merriweather',serif;font-weight:700;font-size:11px;display:flex;align-items:center;justify-content:center}
.hero-title{left:0;top:232px;width:1152px;text-align:center;font-family:'Merriweather',serif;font-weight:700;font-size:49px;line-height:60px;color:var(--white)}
.hero-sub{left:0;top:374px;width:1152px;text-align:center;font-size:13px;line-height:19px;color:var(--white)}
.hero-sub b{color:var(--orange);text-decoration:underline}
.dot{top:478px;width:13px;height:13px;border-radius:50%;background:var(--white)}
.dot.active{box-shadow:inset 0 0 0 3.5px var(--white);background:var(--orange)}
.features{left:0;top:526px;width:1152px;height:122px;background:var(--orange)}
.feature-icon{top:571px}
.feature-title{top:569px;font-weight:700;font-size:14.5px;color:var(--white)}
.feature-text{top:589px;font-size:13px;color:var(--white)}
.photo{border-radius:1px}
.about-eyebrow{left:671px;top:746px;font-family:'Merriweather',serif;font-weight:700;font-size:13.5px;color:var(--blue)}
.about-title{left:669px;top:776px;font-family:'Merriweather',serif;font-size:25.5px;line-height:36px;color:var(--navy)}
.about-text{left:668px;top:860px;width:340px;height:92px;overflow:hidden;font-size:12px;line-height:19.2px;color:var(--muted)}
.about-list{left:670px;top:992px;list-style:none;font-family:'Merriweather',serif;font-size:13px;line-height:28px;color:var(--blue)}
.about-cta{left:669px;top:1112px;width:132px;height:40px}
</style>
</head>
<body>
<header class="abs site-header">
  <div class="abs brand"><span class="brand-dot"></span>Corvexa</div>
  <nav class="main-nav">
    <a class="active" style="left:353px">Home</a>
    <a style="left:416px">Services</a>
    <a style="left:494px">Packages</a>
    <a style="left:579px">About Us</a>
    <a style="left:660px">Contact Us</a>
  </nav>
  <a class="abs btn header-cta">Get Started</a>
</header>

<section class="abs hero" role="img" aria-label="Woman smiling while working on a laptop in a cafe"></section>
<div class="abs hero-badge">Welcome To Corvexa</div>
<h1 class="abs hero-title">Take Controll With<br>Pure Fiber Broadband</h1>
<p class="abs hero-sub">Choose Corvexa best monthly plan<br>Starting From <b>$20</b></p>
<span class="abs dot active" style="left:544px"></span>
<span class="abs dot" style="left:570px"></span>
<span class="abs dot" style="left:596px"></span>

<section class="abs features"></section>
<svg class="abs feature-icon" style="left:178px" width="28" height="30" viewBox="0 0 28 30" fill="none" stroke="#fff" stroke-width="2.5"><path d="M2 2l12 13L2 28M13 2l12 13-12 13"/></svg>
<div class="abs feature-title" style="left:225px">Faster Internet</div>
<div class="abs feature-text" style="left:225px">Up to 15x faster than DSL</div>
<svg class="abs feature-icon" style="left:497px" width="28" height="30" viewBox="0 0 28 30" fill="none" stroke="#fff" stroke-width="1.6"><rect x="1" y="6" width="26" height="22"/><path d="M1 12h26M7 2v7M21 2v7M6 18h5v5H6z"/></svg>
<div class="abs feature-title" style="left:543px">More Reliable</div>
<div class="abs feature-text" style="left:543px">Best experiance than DSL</div>
<svg class="abs feature-icon" style="left:815px" width="30" height="30" viewBox="0 0 30 30" fill="none" stroke="#fff" stroke-width="1.6"><circle cx="17" cy="7" r="5.5"/><path d="M17 4v6M2 22l6-5h8a2 2 0 010 4h-5M10 26l4 2 13-9-2-2-8 4M2 22l4 5"/></svg>
<div class="abs feature-title" style="left:862px">Best Price</div>
<div class="abs feature-text" style="left:862px">Low price in town</div>

<div class="abs photo" style="left:90px;top:744px;width:234px;height:211px;background:linear-gradient(135deg,#c9c9c7 0%,#8a6a4e 45%,#5b4330 100%)" role="img" aria-label="Smartwatch on a wrist"></div>
<div class="abs photo" style="left:90px;top:982px;width:234px;height:184px;background:linear-gradient(160deg,#2c3c6a 0%,#c7a48a 50%,#8c7460 100%)" role="img" aria-label="Hands holding a phone above a laptop keyboard"></div>
<div class="abs photo" style="left:358px;top:744px;width:265px;height:405px;background:linear-gradient(180deg,#6b4a2e 0%,#3a2a1e 45%,#1c1714 100%)" role="img" aria-label="Hand holding a phone in a lit corridor"></div>

<div class="abs about-eyebrow">Welcome To Corvexa</div>
<h2 class="abs about-title" style="font-weight:400">Experiance what Broadband<br>should be never before</h2>
<p class="abs about-text">Lorem Ipsum is simply dummy text of the printing and typesetting industry. Lorem Ipsum has been the industry's standard dummy text ever since the 1500s, when an unknown printer took a galley of type and scrambled it to make a type specimen book.</p>
<ul class="abs about-list">
  <li>Supefast and best internet</li>
  <li>More chanel on TV cable</li>
  <li>Supefast and best internet</li>
</ul>
<a class="abs btn about-cta">Get Started</a>
</body>
</html>
```